Brenmoor Group needs a business card

I would like the card to be simple but modern and elegant.
I like black and white.
or black and gold.
we are a private finance lender and also are involved in property and property developments.

please look at the business card photos i provided i would like B.G only one one side and all the other details on the other side use fonts that tie in with my theme.

Industry/Entity Type

Finance

Contact Information for Business Card

Brenmoor Group (B.G) Callum Brenmoor M: 0418396152 E: callumbren@quivomail.com

Font styles to use
Other font styles liked:
• Use fonts that would reflect our business

Colors
000000
ffffff

Requirements
Must have
• one side of details
• other side has either B.G or Brenmoor Group like in the photos provided

```html
<!DOCTYPE html>
<html lang="en">
<head>
<meta charset="utf-8">
<title>Brenmoor Group – Business Card</title>
<link href="https://fonts.googleapis.com/css2?family=Questrial&display=swap" rel="stylesheet">
<style>
  :root {
    --stage: #e4e4e6;
    --card-black: #0d0d0d;
    --gold: #e3a41f;
    --gold-line: #9a6b16;
    --shadow: rgba(0, 0, 0, 0.28);
  }
  * { margin: 0; padding: 0; box-sizing: border-box; }
  html, body {
    width: 1200px;
    height: 800px;
    overflow: hidden;
    background: var(--stage);
    font-family: "Questrial", sans-serif;
  }
  .stage {
    position: relative;
    width: 1200px;
    height: 800px;
  }
  .card {
    position: absolute;
    top: 250px;
    width: 520px;
    height: 300px;
    background:
      radial-gradient(ellipse at 20% 10%, #262626 0%, transparent 45%),
      radial-gradient(ellipse at 85% 90%, #222 0%, transparent 40%),
      var(--card-black);
    box-shadow: 0 14px 30px var(--shadow);
  }
  .card--front { left: 50px; }
  .card--back { left: 630px; }
  .card__frame {
    position: absolute;
    inset: 28px 34px;
    border: 1px solid var(--gold-line);
  }

  /* Front */
  .front__accent-area {
    position: absolute;
    width: 140px;
    height: 40px;
    background: linear-gradient(100deg, transparent, rgba(227, 164, 31, 0.08), transparent);
  }
  .front__accent-area--top { left: 92px; top: 88px; }
  .front__accent-area--bottom { right: 92px; bottom: 88px; }
  .front__name {
    position: absolute;
    left: 0;
    right: 0;
    top: 50%;
    transform: translateY(-50%);
    text-align: center;
    color: var(--gold);
    font-size: 34px;
    font-weight: 400;
    letter-spacing: 4px;
    text-transform: uppercase;
  }

  /* Back */
  .contact {
    position: absolute;
    left: 62px;
    top: 46px;
    color: var(--gold);
  }
  .contact__rail {
    position: absolute;
    left: 0;
    top: 0;
    width: 30px;
    height: 150px;
    overflow: visible;
  }
  .contact__list {
    list-style: none;
    margin-left: 14px;
    padding-top: 2px;
  }
  .contact__item {
    display: flex;
    align-items: center;
    gap: 8px;
    height: 22px;
    font-size: 11px;
    letter-spacing: 0.6px;
    text-transform: uppercase;
  }
  .contact__item--company {
    font-size: 15px;
    height: 26px;
    padding-left: 4px;
    letter-spacing: 0.4px;
  }
  .contact__icon {
    width: 10px;
    height: 10px;
    flex: none;
  }
</style>
</head>
<body>
<main class="stage">

  <section class="card card--front" aria-label="Card front">
    <div class="card__frame"></div>
    <div class="front__accent-area front__accent-area--top" role="img" aria-label="Decorative gold diagonal accent"></div>
    <h1 class="front__name">Brenmoor Group</h1>
    <div class="front__accent-area front__accent-area--bottom" role="img" aria-label="Decorative gold diagonal accent"></div>
  </section>

  <section class="card card--back" aria-label="Card back">
    <div class="card__frame"></div>
    <div class="contact">
      <svg class="contact__rail" viewBox="0 0 30 150" aria-hidden="true">
        <circle cx="4" cy="10" r="4" fill="#e3a41f"/>
        <line x1="4" y1="10" x2="4" y2="118" stroke="#9a6b16" stroke-width="1"/>
        <circle cx="4" cy="118" r="4" fill="#e3a41f"/>
        <line x1="4" y1="118" x2="4" y2="150" stroke="#9a6b16" stroke-width="1"/>
      </svg>
      <ul class="contact__list">
        <li class="contact__item contact__item--company">Brenmoor Group</li>
        <li class="contact__item">
          <svg class="contact__icon" viewBox="0 0 10 10" aria-hidden="true">
            <circle cx="5" cy="3" r="2.4" fill="#e3a41f"/>
            <path d="M0.5 10 Q5 4.5 9.5 10 Z" fill="#e3a41f"/>
          </svg>
          Callum Brenmoor
        </li>
        <li class="contact__item">
          <svg class="contact__icon" viewBox="0 0 10 10" aria-hidden="true">
            <rect x="2.2" y="0.5" width="5.6" height="9" rx="1" fill="none" stroke="#e3a41f" stroke-width="1"/>
            <line x1="4" y1="8" x2="6" y2="8" stroke="#e3a41f" stroke-width="0.8"/>
          </svg>
          0418396152
        </li>
        <li class="contact__item">
          <svg class="contact__icon" viewBox="0 0 10 10" aria-hidden="true">
            <rect x="0.5" y="2" width="9" height="6.5" fill="#e3a41f"/>
            <path d="M0.5 2 L5 5.6 L9.5 2" fill="none" stroke="#0d0d0d" stroke-width="0.9"/>
          </svg>
          callumbren@quivomail.com
        </li>
      </ul>
    </div>
  </section>

</main>
</body>
</html>
```